Dr Delwyn's Letterhead

I need a professional neat letterhead incorporating my professional information, university titles and qualifications. I have attached my 3 recent ones which contain all the necessary information that needs to be included. I am happy for the information to be a side bar left or right, or as a header/footer combination.

Hello all

I have now made a 2nd and 3rd prize so please submit

Reason: Now there is a 2nd and 3rd place so I can take 3 designs

University

```html
<!DOCTYPE html>
<html lang="en">
<head>
<meta charset="utf-8">
<title>Dr Delwyn Letterhead</title>
<link href="https://fonts.googleapis.com/css2?family=Crimson+Text:wght@400;700&family=PT+Sans:wght@400&display=swap" rel="stylesheet">
<style>
  :root {
    --backdrop: #e4e1dc;
    --paper: #ffffff;
    --ink: #2b2b2b;
    --ink-soft: #3a3a3a;
    --band: #3f3f3f;
    --band-text: #ffffff;
    --rule: #555555;
    --badge-a: #c9a640;
    --badge-b: #b8302c;
    --mark-square: #1f5f5a;
  }
  * { margin: 0; padding: 0; box-sizing: border-box; }
  html, body { width: 961px; height: 1200px; overflow: hidden; background: var(--backdrop); }
  body { position: relative; font-family: "Crimson Text", Georgia, serif; color: var(--ink); }

  .letterhead {
    position: absolute; left: 77px; top: 86px; width: 812px; height: 1051px;
    background: var(--paper); box-shadow: 0 2px 10px rgba(0,0,0,.18);
  }
  .identity { position: absolute; left: 26px; top: 24px; }
  .identity__name { font-size: 32px; font-weight: 400; line-height: 1; letter-spacing: .2px; }
  .identity__quals { margin-top: 4px; font-size: 15.5px; line-height: 22px; color: var(--ink-soft); }
  .identity__contact {
    margin-top: 5px; display: flex; align-items: center; gap: 8px;
    font-family: "PT Sans", Arial, sans-serif; font-size: 15px; color: var(--ink);
  }
  .contact-item { display: flex; align-items: center; gap: 6px; margin-right: 4px; }
  .contact-item svg { width: 16px; height: 16px; }
  .contact-item--fax { margin-left: 6px; }
  .contact-item--fax svg { width: 20px; height: 16px; }

  .practice { position: absolute; font-size: 15px; line-height: 19.5px; color: var(--ink-soft); font-style: normal; }
  .practice__title { font-weight: 700; color: var(--ink); }
  .practice--central { right: 207px; top: 44px; text-align: right; }
  .practice--side { left: 628px; top: 23px; }
  .practice--side .practice__gap { margin-top: 5px; }
  .practice-divider { position: absolute; left: 616px; top: 25px; width: 1px; height: 100px; background: var(--rule); }

  .footer-band {
    position: absolute; left: 0; bottom: 0; width: 812px; height: 101px; background: var(--band);
    color: var(--band-text);
  }
  .roles { position: absolute; left: 18px; top: 13px; font-size: 13px; line-height: 16.5px; }
  .badge { position: absolute; top: 13px; }
  .badge--one { left: 467px; width: 50px; height: 59px; background: var(--paper); padding: 3px; }
  .badge--two { left: 535px; width: 66px; height: 59px; background: var(--paper); padding: 4px 12px; }
  .badge svg { width: 100%; height: 100%; display: block; }
  .college-mark {
    position: absolute; left: 620px; top: 13px; width: 180px; height: 59px; background: var(--paper);
    display: flex; align-items: center; justify-content: center; gap: 10px;
    font-size: 20px; font-weight: 400; color: var(--ink); letter-spacing: .3px; line-height: 1.05;
  }
  .college-mark__square { width: 26px; height: 26px; background: var(--mark-square); flex: none; }
  .provider {
    position: absolute; left: 520px; top: 74px; font-size: 13.5px; font-weight: 700; letter-spacing: .2px;
  }
</style>
</head>
<body>
  <article class="letterhead">
    <header>
      <div class="identity">
        <h1 class="identity__name">Dr. Tomas Delwyn</h1>
        <p class="identity__quals">BSc Med, MBBS (Hons 1) NVU<br>MSc, FNCS (Oto-HNS)</p>
        <div class="identity__contact">
          <span class="contact-item">
            <svg viewBox="0 0 16 16" aria-hidden="true"><circle cx="8" cy="8" r="7" fill="none" stroke="#2b2b2b" stroke-width="1.2"/><path d="M5.6 4.2c.6-.3 1.1 0 1.3.5l.5 1.3c.2.4 0 .8-.3 1l-.5.4c.4.9 1 1.6 1.9 2l.4-.5c.3-.3.7-.4 1-.2l1.2.6c.4.2.6.8.3 1.3-.5.9-1.6 1.2-2.6.7-1.9-.9-3.3-2.5-4-4.4-.3-1.1 0-2.2.8-2.7z" fill="#2b2b2b"/></svg>
            95510284
          </span>
          <span class="contact-item">
            <svg viewBox="0 0 16 16" aria-hidden="true"><circle cx="8" cy="8" r="7" fill="none" stroke="#2b2b2b" stroke-width="1.2"/><path d="M5.6 4.2c.6-.3 1.1 0 1.3.5l.5 1.3c.2.4 0 .8-.3 1l-.5.4c.4.9 1 1.6 1.9 2l.4-.5c.3-.3.7-.4 1-.2l1.2.6c.4.2.6.8.3 1.3-.5.9-1.6 1.2-2.6.7-1.9-.9-3.3-2.5-4-4.4-.3-1.1 0-2.2.8-2.7z" fill="#2b2b2b"/></svg>
            95517390
          </span>
          <span class="contact-item contact-item--fax">
            <svg viewBox="0 0 20 16" aria-hidden="true"><rect x="5" y="1" width="10" height="5" fill="#2b2b2b"/><rect x="1" y="6" width="18" height="9" rx="1.5" fill="#2b2b2b"/><rect x="4" y="9" width="12" height="1.4" fill="#fff"/><rect x="4" y="12" width="12" height="1.4" fill="#fff"/></svg>
            95519462
          </span>
        </div>
      </div>

      <address class="practice practice--central">
        <div class="practice__title">Marlowe Specialist Centre</div>
        <div>18 Marlowe Parade</div>
        <div>Kestrel Vale NSW 2190</div>
      </address>

      <div class="practice-divider"></div>

      <address class="practice practice--side">
        <div class="practice__title">Riverbend Medical Centre</div>
        <div>208/64 Ashgrove Rd.</div>
        <div>Linfield NSW 2173</div>
        <div class="practice__gap">42 Carrow Street</div>
        <div>Halden 2781</div>
      </address>
    </header>

    <footer class="footer-band">
      <p class="roles">
        Consultant ENT/Head and Neck Surgeon<br>
        Elmstead Cancer Care Centre<br>
        Linfield Hospital and Western Plains Health District (WPHD)<br>
        Senior Lecturer, University of Northvale (UNV) &amp; Western Plains (UWP)
      </p>
      <div class="badge badge--one">
        <svg viewBox="0 0 44 53" role="img" aria-label="University badge"><path d="M2 2h40v26c0 13-10 21-20 23C12 49 2 41 2 28z" fill="var(--badge-a)"/></svg>
      </div>
      <div class="badge badge--two">
        <svg viewBox="0 0 42 51" role="img" aria-label="University badge"><path d="M2 2h38v24c0 12-9 20-19 22C11 46 2 38 2 26z" fill="var(--badge-b)"/></svg>
      </div>
      <div class="college-mark">
        <span class="college-mark__square"></span>
        <span>Northvale<br>Surgical College</span>
      </div>
      <p class="provider">Provider 7310846K, 582071PL, 582071QM</p>
    </footer>
  </article>
</body>
</html>
```